Wordpress site needed for company's Healthcare Web App

Healthcare web app needs wordpress web design for web site that provides an overview of the product, a page explaining key features, a blog, a press release announcement section, customer testimonials, contact us, sign up page, invite friends.

The website should use the color scheme including in the logo. This web site is not the app, this website will be used to introduce the app.

Target Market(s)

Doctors, enterprise healthcare professionals, patients who will use patient portals to access their health info. (not the app itself, but this site introduces the app)

Industry/Entity Type

Health Care

Coding

Coded - Design and coding required

Number of Pages Required

5+ page

Font styles to use
Sans Serif

Requirements
Must have
• This is a Wordpress based site.
• Product Overview, Key Product Features, Blog, Press Releases, Events, Embedded Videos explaining the product and demo'ing features, Sign Up Page for people interested,
Nice to have
• Uplifting Hero Image for Healthcare Tech, color scheme fitting with logo

```html
<!DOCTYPE html>
<html lang="en">
<head>
<meta charset="utf-8">
<title>CareLedger – Healthcare Web App</title>
<link rel="stylesheet" href="https://fonts.googleapis.com/css2?family=Roboto:wght@300;400;500&display=swap">
<style>
:root{
  --teal:#4b9cb5;
  --teal-dark:#3f8ba3;
  --ink:#2f3236;
  --text:#6b6e72;
  --muted:#8c8f93;
  --line:#dcdcdc;
  --soft-bg:#f7f7f7;
  --white:#ffffff;
  --bar:#7f8184;
}
*{margin:0;padding:0;box-sizing:border-box}
html,body{width:1200px;height:2195px;overflow:hidden}
body{position:relative;font-family:'Roboto',Arial,sans-serif;color:var(--text);background:var(--white)}
.abs{position:absolute}

/* Header */
.site-header{position:absolute;left:0;top:0;width:1200px;height:57px;background:var(--white);border-bottom:1px solid #e6e6e6;z-index:2}
.brand{position:absolute;left:88px;top:14px;display:flex;align-items:center;gap:8px}
.brand-mark{width:26px;height:26px;border:2px solid var(--teal);border-radius:4px}
.brand-name{font-size:19px;font-weight:500;color:var(--teal);letter-spacing:-.2px}
.main-nav{position:absolute;top:0;left:0;height:57px;width:1200px}
.main-nav a{position:absolute;top:20px;font-size:13px;color:#5d6064;text-decoration:none}
.nav-home{position:absolute;left:575px;top:20px}
.btn-signup{position:absolute;left:1018px;top:13px;width:93px;height:31px;border:1px solid #cfcfcf;border-radius:16px;font-size:12px;color:#4a4d51;text-align:center;line-height:29px}

/* Hero */
.hero{position:absolute;left:0;top:57px;width:1200px;height:550px;background:linear-gradient(100deg,#a8b7bd 0%,#b4c4c9 35%,#a9bfc6 60%,#9fb7bf 100%)}
.hero-copy{position:absolute;left:0;top:210px;width:1200px;text-align:center;color:var(--white)}
.hero-title{font-size:41px;font-weight:300;letter-spacing:-.3px}
.hero-sub{margin-top:8px;font-size:16px;font-weight:300}
.btn-pill{display:inline-block;background:var(--teal);color:var(--white);font-size:13px;border-radius:18px;text-align:center}
.hero .btn-pill{margin-top:15px;width:132px;height:33px;line-height:33px}
.hero-dots{position:absolute;left:580px;top:484px;display:flex;gap:6px}
.hero-dots span{width:8px;height:8px;border-radius:50%;background:#c5d2d6}
.hero-dots .active{background:var(--teal)}

/* Features */
.features{position:absolute;left:0;top:607px;width:1200px;height:426px}
.feature-label{position:absolute;font-size:12.5px;color:#5a5d61;white-space:nowrap}
.welcome{position:absolute;left:600px;top:88px;width:520px}
.welcome-kicker{font-size:18px;font-weight:300;color:var(--ink)}
.welcome-title{font-size:35px;font-weight:300;color:var(--ink);margin-top:2px}
.welcome-title span{color:var(--teal)}
.welcome p{font-size:12.5px;line-height:20px;margin-top:12px;color:var(--text)}
.welcome p + p{margin-top:12px}
.welcome .btn-pill{position:absolute;left:0;top:246px;width:126px;height:34px;line-height:34px}

/* Blog & events */
.news{position:absolute;left:0;top:1033px;width:1200px;height:461px;background:var(--soft-bg)}
.news-divider{position:absolute;left:594px;top:35px;width:1px;height:407px;background:#d6d6d6}
.date-badge{position:absolute;left:564px;top:66px;width:58px;height:58px;border-radius:50%;background:var(--teal);color:var(--white);text-align:center}
.date-badge b{display:block;font-size:21px;font-weight:500;line-height:22px;margin-top:11px}
.date-badge small{font-size:9px}
.news-heading{position:absolute;top:80px;font-size:22px;font-weight:300;color:var(--ink)}
.news-card{position:absolute;top:117px;width:375px;height:271px;background:var(--white);border:1px solid #e2e2e2}
.news-card .photo{width:100%;height:207px}
.news-card h3{font-size:13.5px;font-weight:400;color:var(--ink);margin:16px 0 0 21px}
.news-meta{display:flex;align-items:center;gap:10px;margin:7px 0 0 21px;font-size:12px;color:#6a6d71}
.blog-photo{background:linear-gradient(180deg,#e3e6ea 0%,#d6c4bb 55%,#9dc0d8 100%)}
.event-photo{background:linear-gradient(90deg,#7ea36b 0%,#a9b99a 45%,#c7b9aa 70%,#9fb28e 100%)}

/* Video */
.video-band{position:absolute;left:0;top:1494px;width:1200px;height:404px;background:linear-gradient(90deg,#6fb0c5 0%,#5ea6bd 45%,#64a7bd 70%,#5a9fb6 100%)}
.video-title{position:absolute;left:0;top:122px;width:1200px;text-align:center;font-size:30px;font-weight:300;color:var(--white)}

/* Footer */
.site-footer{position:absolute;left:0;top:1898px;width:1200px;height:250px;background:var(--white)}
.footer-brand{position:absolute;left:88px;top:42px;display:flex;align-items:center;gap:8px}
.footer-about{position:absolute;left:88px;top:86px;width:235px;font-size:11px;line-height:17px}
.footer-col{position:absolute;top:50px}
.footer-col h4{font-size:15px;font-weight:400;color:#55585c;margin-bottom:12px}
.link-list li{list-style:none;font-size:11px;color:#5f6266;height:24px;display:flex;align-items:center;gap:10px}
.press-item{width:237px;font-size:11px;line-height:17px;color:#5f6266;padding-bottom:10px}
.press-item time{display:block;color:var(--teal);margin-top:2px}
.press-item + .press-item{border-top:1px solid #e2e2e2;padding-top:10px}
.contact li{list-style:none;font-size:11px;line-height:17px;color:#5f6266;display:flex;gap:8px;margin-bottom:11px}
.contact svg{flex:none;margin-top:3px}

.bottom-bar{position:absolute;left:0;top:2148px;width:1200px;height:47px;background:var(--bar);color:var(--white);font-size:11px}
.bottom-bar .copy{position:absolute;left:88px;top:17px}
.bottom-bar .legal{position:absolute;right:90px;top:17px}
.to-top{position:absolute;left:1143px;top:2130px;width:34px;height:34px;border-radius:50%;background:var(--teal);z-index:3}
</style>
</head>
<body>

<header class="site-header">
  <div class="brand"><span class="brand-mark"></span><span class="brand-name">CareLedger</span></div>
  <nav class="main-nav">
    <svg class="nav-home" width="13" height="12" viewBox="0 0 13 12"><path d="M6.5 0 0 5.5h2V12h3.2V8h2.6v4H11V5.5h2z" fill="#4b9cb5"/></svg>
    <a style="left:613px">Product</a>
    <a style="left:687px">Features</a>
    <a style="left:766px">Blog</a>
    <a style="left:821px">Press</a>
    <a style="left:880px">Releases</a>
    <a style="left:961px">Events</a>
    <span class="btn-signup">Sign Up</span>
  </nav>
</header>

<section class="hero" role="img" aria-label="Hero photo: a smiling doctor with a stethoscope touching a holographic medical data interface, under a soft teal wash">
  <div class="hero-copy">
    <h1 class="hero-title">Healthcare Web App</h1>
    <p class="hero-sub">Lorem ipsum dolor sit amet, consectetuer adipiscing elit aenean commodo</p>
    <span class="btn-pill">Invite friends</span>
  </div>
  <div class="hero-dots"><span></span><span class="active"></span><span></span></div>
</section>

<section class="features">
  <svg class="abs" style="left:0;top:0" width="600" height="426" viewBox="0 0 600 426">
    <g stroke="#9a9da1" stroke-width="1" stroke-dasharray="2 3" fill="none">
      <line x1="159" y1="91" x2="234" y2="91"/>
      <line x1="383" y1="91" x2="460" y2="91"/>
      <line x1="157" y1="233" x2="237" y2="233"/>
      <line x1="383" y1="233" x2="462" y2="233"/>
      <line x1="310" y1="265" x2="310" y2="313"/>
    </g>
    <circle cx="310" cy="166" r="100" fill="none" stroke="#4b9cb5" stroke-width="3"/>
    <g fill="#4b9cb5">
      <circle cx="239" cy="91" r="7"/><circle cx="381" cy="91" r="7"/>
      <circle cx="237" cy="233" r="7"/><circle cx="383" cy="233" r="7"/>
      <circle cx="310" cy="266" r="7"/>
    </g>
    <text x="310" y="154" text-anchor="middle" font-family="Roboto, sans-serif" font-size="13" fill="#6b6e72" letter-spacing=".5">PRODUCT</text>
    <text x="310" y="186" text-anchor="middle" font-family="Roboto, sans-serif" font-weight="300" font-size="28" fill="#4b9cb5">Features</text>
    <g fill="#fff" stroke="#bfc2c5" stroke-width="1.2">
      <circle cx="142" cy="91" r="18"/><circle cx="478" cy="91" r="18"/>
      <circle cx="140" cy="233" r="18"/><circle cx="480" cy="233" r="18"/>
      <circle cx="310" cy="331" r="18"/>
    </g>
    <g fill="#5a5d61">
      <ellipse cx="142" cy="85" rx="7" ry="2.5"/><rect x="135" y="86" width="14" height="3"/><rect x="135" y="91" width="14" height="3"/><rect x="135" y="96" width="14" height="3"/>
      <rect x="471" y="83" width="13" height="11" fill="none" stroke="#5a5d61" stroke-width="2"/><rect x="474" y="94" width="3" height="6"/><rect x="470" y="99" width="10" height="2"/>
      <circle cx="140" cy="233" r="8"/><path d="M136 233l3 3 5-6" stroke="#fff" stroke-width="2" fill="none"/>
      <rect x="472" y="236" width="3" height="5"/><rect x="477" y="232" width="3" height="9"/><rect x="482" y="228" width="3" height="13"/><path d="M471 231l6-5 4 2 6-5" stroke="#5a5d61" stroke-width="1.5" fill="none"/>
      <circle cx="306" cy="326" r="3.5"/><circle cx="314" cy="326" r="3.5"/><path d="M300 338a6 6 0 0 1 12 0zM308 338a6 6 0 0 1 12 0z"/>
    </g>
  </svg>
  <span class="feature-label" style="left:117px;top:121px">Finance</span>
  <span class="feature-label" style="left:432px;top:122px">Info Technology</span>
  <span class="feature-label" style="left:88px;top:265px">Quality Assurance</span>
  <span class="feature-label" style="left:448px;top:268px">Marketing</span>
  <span class="feature-label" style="left:259px;top:364px">Human Resource</span>

  <div class="welcome">
    <p class="welcome-kicker">Welcome To</p>
    <h2 class="welcome-title">Care <span>Ledger</span></h2>
    <p>Lorem ipsum dolor sit amet, consectetuer adipiscing elit. Aenean commodo ligula eget dolor. Aenean massa. Cum sociis natoque penatibus et magnis dis parturient montes, nascetur ridiculus mus. Donec quam felis, ultricies nec.</p>
    <p>Ultricies nec, pellentesque eu, pretium quis, sem. Nulla consequat massa quis enim. Donec pede justo, fringilla vel, aliquet nec, vulputate eget, arcu. In enim justo, rhoncus ut, imperdiet a, venenatis vitae, justo. Nullam dictum felis eu pede mollis pretium. Integer tincidunt. Cras dapibus. Vivamus elementum semper nisi.</p>
    <span class="btn-pill">Read More</span>
  </div>
</section>

<section class="news">
  <div class="news-divider"></div>
  <div class="date-badge"><b>22</b><small>Nov</small></div>
  <h2 class="news-heading" style="left:135px">Blog</h2>
  <h2 class="news-heading" style="left:684px">Events</h2>
  <article class="news-card" style="left:136px">
    <div class="photo blog-photo" role="img" aria-label="Photo of a smiling family of four lying together on a bed"></div>
    <h3>Nullam dictum felis eu pede</h3>
    <div class="news-meta">
      <svg width="11" height="11" viewBox="0 0 11 11"><rect x=".5" y="1.5" width="10" height="9" fill="none" stroke="#b5b8bb"/><rect x=".5" y="1.5" width="10" height="2.5" fill="#b5b8bb"/></svg>
      <span>02/15/2016</span>
      <svg style="margin-left:120px" width="13" height="11" viewBox="0 0 13 11"><path d="M1 1h11v7H5l-3 2.5V8H1z" fill="none" stroke="#9a9da1"/></svg>
    </div>
  </article>
  <article class="news-card" style="left:688px">
    <div class="photo event-photo" role="img" aria-label="Photo of a woman drinking water from a bottle outdoors in a park"></div>
    <h3>Maecenas tempus tellus eget</h3>
    <div class="news-meta">
      <svg width="11" height="11" viewBox="0 0 11 11"><rect x=".5" y="1.5" width="10" height="9" fill="none" stroke="#b5b8bb"/><rect x=".5" y="1.5" width="10" height="2.5" fill="#b5b8bb"/></svg>
      <span>02/15/2016</span>
    </div>
  </article>
</section>

<section class="video-band" role="img" aria-label="Background photo of a smiling doctor and a consultation scene under a teal overlay">
  <h2 class="video-title">Watch Video</h2>
  <svg class="abs" style="left:537px;top:170px" width="126" height="126" viewBox="0 0 126 126">
    <circle cx="63" cy="63" r="63" fill="#ffffff" fill-opacity=".2"/>
    <circle cx="63" cy="63" r="42" fill="#fff"/>
    <g fill="none" stroke="#5a5d61" stroke-width="1.6">
      <rect x="46" y="52" width="34" height="22"/>
      <line x1="53" y1="52" x2="53" y2="74"/><line x1="73" y1="52" x2="73" y2="74"/>
      <line x1="53" y1="63" x2="73" y2="63"/>
      <line x1="46" y1="58" x2="53" y2="58"/><line x1="46" y1="68" x2="53" y2="68"/>
      <line x1="73" y1="58" x2="80" y2="58"/><line x1="73" y1="68" x2="80" y2="68"/>
    </g>
  </svg>
</section>

<footer class="site-footer">
  <div class="footer-brand"><span class="brand-mark"></span><span class="brand-name">CareLedger</span></div>
  <p class="footer-about">Lorem ipsum dolor sit amet, consectetuer adipiscing elit. Aenean commodo ligula eget dolor. Cum sociis natoque penatibus et magnis dis parturient .</p>

  <div class="footer-col" style="left:408px">
    <h4>Useful Links</h4>
    <ul class="link-list">
      <li><svg width="11" height="8" viewBox="0 0 11 8"><path d="M0 4h10M7 1l3 3-3 3" stroke="#5f6266" fill="none"/></svg>Product</li>
      <li><svg width="11" height="8" viewBox="0 0 11 8"><path d="M0 4h10M7 1l3 3-3 3" stroke="#5f6266" fill="none"/></svg>Features</li>
      <li><svg width="11" height="8" viewBox="0 0 11 8"><path d="M0 4h10M7 1l3 3-3 3" stroke="#5f6266" fill="none"/></svg>Blog</li>
      <li><svg width="11" height="8" viewBox="0 0 11 8"><path d="M0 4h10M7 1l3 3-3 3" stroke="#5f6266" fill="none"/></svg>Press</li>
      <li><svg width="11" height="8" viewBox="0 0 11 8"><path d="M0 4h10M7 1l3 3-3 3" stroke="#5f6266" fill="none"/></svg>Releases</li>
      <li><svg width="11" height="8" viewBox="0 0 11 8"><path d="M0 4h10M7 1l3 3-3 3" stroke="#5f6266" fill="none"/></svg>Events</li>
    </ul>
  </div>

  <div class="footer-col" style="left:582px">
    <h4>Press Releases</h4>
    <div class="press-item">Lorem ipsum dolor sit amet, consectetuer adipiscing elit aenean commodo .<time>14 / 4 / 2016</time></div>
    <div class="press-item">Lorem ipsum dolor sit amet, consectetuer adipiscing elit aenean commodo .<time>14 / 4 / 2016</time></div>
  </div>

  <div class="footer-col" style="left:853px">
    <h4>Contact Us</h4>
    <ul class="contact">
      <li><svg width="9" height="12" viewBox="0 0 9 12"><path d="M4.5 0A4.5 4.5 0 0 0 0 4.5C0 8 4.5 12 4.5 12S9 8 9 4.5A4.5 4.5 0 0 0 4.5 0z" fill="#4b9cb5"/><circle cx="4.5" cy="4.5" r="1.6" fill="#fff"/></svg><span>4820 W. Juniper Park Ave.<br>#210 Mesa Hills, TX 75001</span></li>
      <li><svg width="10" height="10" viewBox="0 0 10 10"><path d="M2 0l2 2.5-1.2 1.3a6 6 0 0 0 3.4 3.4L7.5 6 10 8l-1.5 2C4 10 0 6 0 1.5z" fill="#4b9cb5"/></svg><span>Phone: 555-013-2760</span></li>
      <li><svg width="11" height="8" viewBox="0 0 11 8"><rect width="11" height="8" fill="#4b9cb5"/><path d="M0 0l5.5 4.5L11 0" stroke="#fff" fill="none"/></svg><span>Email: hello@careledger.example</span></li>
    </ul>
  </div>
</footer>

<div class="bottom-bar">
  <span class="copy">Copyright 2016 | All right Reserved</span>
  <span class="legal">Terms &amp; Conditions | Privacy Policy</span>
</div>
<svg class="to-top" viewBox="0 0 34 34"><path d="M13 19l4-4 4 4" stroke="#fff" stroke-width="1.6" fill="none"/></svg>

</body>
</html>
```